Business card design for web travel company

Hi
we'd like to receive some proposal for a business card design.
Quindra is a private travel club, dedicated to all travel lovers, with unique offers for exclusive destinations all around the world. At Quindra you can find a wide range of offers for resorts, boutique hotels and travel packages at the best guaranteed price available on the market. The convenience of the offer is guaranteed by a private sales model: offers are available for a limited time only and they are personally chosen by Quindra's qualified team of travel experts.
We offer only exclusive hotels with discounted prices but we are not an outlet or a discount supermarket: the design should reflect our connection with luxury, exclusivity using the same style of our website www.quindra-example.com.
We want to make sure that when we'll present ourself to our business partner they will feel immediately which is our brand positioning giving them also a sense of an affordable and reliable partner.
In attachment you can also find our brand guidelines (please note that we are NOT USING ANY MORE THE TAG LINE "Five star outlet" mentioned in it).
The info to be inserted are:
Name Surname
Job Title
Tel
Mobile (when needed)
Email
Quindra S.r.l.
Via Pietro Lanzi 27
20137 Milano

```html
<!DOCTYPE html>
<html lang="en">
<head>
<meta charset="utf-8">
<title>Quindra business card</title>
<link rel="stylesheet" href="https://fonts.googleapis.com/css2?family=Arimo:wght@400;700&display=swap">
<style>
  :root {
    --backdrop: #e9e6e2;
    --ink: #0b0b0b;
    --paper: #ffffff;
    --gold: #8f8463;
    --gold-light: #c2b48c;
    --hatch: #2b2b2b;
    --muted: #bdbdbd;
  }
  * { margin: 0; padding: 0; box-sizing: border-box; }
  html, body {
    width: 1200px; height: 900px; overflow: hidden;
    background: var(--backdrop);
    font-family: "Arimo", Arial, sans-serif;
  }
  .stage { position: relative; width: 1200px; height: 900px; }
  .card {
    position: absolute; top: 302px;
    width: 520px; height: 296px;
    border-radius: 14px; overflow: hidden;
    box-shadow: 0 2px 6px rgba(0,0,0,.18);
  }
  .card--front { left: 55px; background: var(--paper); }
  .card--back { left: 625px; background: var(--ink); }
  .card__art { position: absolute; inset: 0; width: 100%; height: 100%; }
  .brand-name {
    position: absolute; font-weight: 400; font-size: 50px; letter-spacing: 0.5px; line-height: 1;
  }
  .card--front .brand-name { left: 44px; top: 54px; color: var(--ink); }
  .card--back .brand-name { left: 64px; top: 78px; color: var(--paper); }
  .brand-url {
    position: absolute; left: 92px; top: 136px;
    font-size: 14px; letter-spacing: 1.6px; color: var(--muted);
  }
  .contact {
    position: absolute; left: 310px; top: 178px; color: var(--paper);
  }
  .contact__name { font-weight: 700; font-size: 17.5px; margin-bottom: 7px; }
  .contact__line { font-size: 11.5px; line-height: 16px; }
  .contact__line--gap { margin-top: 7px; }
  .contact__icon { display: inline-block; width: 13px; height: 10px; vertical-align: -1px; margin-right: 3px; }
</style>
</head>
<body>
<div class="stage">

  <section class="card card--front">
    <svg class="card__art" viewBox="0 0 520 296" aria-hidden="true">
      <path d="M0,182 C100,236 190,210 285,146 C375,80 450,58 520,58 L520,72 C450,72 380,82 290,160 C200,240 110,262 0,216 Z" fill="var(--gold)"/>
      <path d="M0,216 C110,262 200,240 290,160 C380,82 450,72 520,72 L520,296 L0,296 Z" fill="var(--ink)"/>
      <path d="M0,216 C110,262 200,240 290,160 C380,82 450,72 520,72" fill="none" stroke="var(--paper)" stroke-width="2.5"/>
    </svg>
    <div class="brand-name">Quindra</div>
    <div class="contact">
      <div class="contact__name">Lorenzo Varesi</div>
      <div class="contact__line">Quindra S.r.l.</div>
      <div class="contact__line">Via Pietro Lanzi 27 20137 Milano</div>
      <div class="contact__line contact__line--gap">
        <svg class="contact__icon" viewBox="0 0 13 10"><path d="M1,4 C1,1 12,1 12,4 L9.5,4.5 L9,3 L4,3 L3.5,4.5 Z M3,5 L10,5 L11,9 L2,9 Z" fill="var(--gold-light)"/></svg>: +23 4567 8910
      </div>
      <div class="contact__line">
        <svg class="contact__icon" viewBox="0 0 13 10"><rect x="1" y="1" width="11" height="8" fill="none" stroke="var(--gold-light)" stroke-width="1.2"/><path d="M1,1 L6.5,6 L12,1" fill="none" stroke="var(--gold-light)" stroke-width="1.2"/></svg>: lorenzo@quindra-example.com
      </div>
    </div>
  </section>

  <section class="card card--back">
    <svg class="card__art" viewBox="0 0 520 296" aria-hidden="true">
      <path d="M0,212 C80,262 160,280 240,248 C330,212 400,110 520,100 L520,116 C405,124 340,226 245,264 C160,296 80,282 0,240 Z" fill="var(--gold)"/>
      <path d="M0,240 C80,282 160,296 245,264 C340,226 405,124 520,116" fill="none" stroke="var(--paper)" stroke-width="2.5"/>
    </svg>
    <svg class="card__art" viewBox="0 0 520 296" role="img" aria-label="Fine diagonal hatching pattern filling the lower band">
      <path d="M0,243 C80,285 160,299 246,267 C341,229 406,127 520,119 L520,296 L0,296 Z" fill="var(--hatch)"/>
    </svg>
    <div class="brand-name">Quindra</div>
    <div class="brand-url">www.quindra-example.com</div>
  </section>

</div>
</body>
</html>
```